Modern Business Card Design for Independent Urban Music Label

We need a card design for an independent urban music label called Copper Tide Records based in London. We develop and promote urban British music artists. We attend lots of high profile events with high profile industry people and want a card that comes across both on-brand and sophisticated, professional, trustworthy. I have attached our logo - please use the black and orange version in the upper left HOWEVER we are open to seeing other colors than the orange used though we want the shape of the logo to remain the same.

Info to please include:
Name
Position
Phone
Email
Website

Additional Info:
Twitter: @CopperTideRecsUK
Insta: @CopperTideRecs

Target Market(s)

Industry professionals and others artists

Industry/Entity Type

Business

Contact Information for Business Card

Info to please include:
Name
Position
Phone
Email
Website

Additional Info:
Twitter: @CopperTideRecsUK
Insta: @CopperTideRecs

Requirements
Must have
• Logo, company name
• Info to please include:
• Name
• Position
• Phone
• Email
• Website
Nice to have
• Twitter: @CopperTideRecsUK
• Insta: @CopperTideRecs
• If it can be done so that it doesn't look cluttered

```html
<!DOCTYPE html>
<html lang="en">
<head>
<meta charset="utf-8">
<title>Copper Tide Records – Business Card</title>
<link rel="stylesheet" href="https://fonts.googleapis.com/css2?family=Oswald:wght@400&family=Questrial&family=Mulish:wght@800&display=swap">
<style>
  :root {
    --copper: #e8864a;
    --ink: #1c1c1c;
    --paper: #ffffff;
    --ghost: #ecebea;
    --backdrop: #e4e2df;
  }
  * { box-sizing: border-box; margin: 0; padding: 0; }
  html, body { width: 1200px; height: 873px; overflow: hidden; }
  body {
    background: var(--backdrop);
    position: relative;
    font-family: "Questrial", sans-serif;
    color: var(--ink);
  }
  .card {
    position: absolute;
    top: 286px;
    width: 520px;
    height: 300px;
    overflow: hidden;
    box-shadow: 0 6px 18px rgba(0,0,0,.18);
  }
  .card--front { left: 60px; background: var(--paper); }
  .card--back { left: 620px; background: var(--copper); }

  .card__ghost-ring {
    position: absolute;
    left: 205px; top: 40px;
    width: 260px; height: 260px;
    border: 14px solid var(--ghost);
    border-radius: 50%;
  }
  .brand-mark {
    position: absolute;
    left: 34px; top: 26px;
    width: 64px; height: 64px;
    border: 5px solid var(--ink);
    border-radius: 50%;
  }
  .brand-name {
    position: absolute;
    font-family: "Oswald", sans-serif;
    font-weight: 400;
    letter-spacing: 1.5px;
    text-transform: uppercase;
    white-space: nowrap;
  }
  .card--front .brand-name {
    left: 34px; top: 236px;
    font-size: 15px;
    line-height: 20px;
    color: var(--copper);
  }
  .holder {
    position: absolute;
    right: 34px; top: 24px;
    font-family: "Mulish", sans-serif;
    font-weight: 800;
    font-size: 17px;
    line-height: 1.35;
  }
  .contacts {
    position: absolute;
    left: 236px; top: 118px;
    list-style: none;
    font-size: 15px;
    white-space: nowrap;
  }
  .contacts li {
    display: flex;
    align-items: center;
    gap: 9px;
    height: 27px;
  }
  .contacts__icon {
    width: 17px; height: 17px;
    flex: none;
  }
  .stripe {
    position: absolute;
    left: 0; bottom: 0;
    width: 100%; height: 34px;
    background: var(--copper);
    color: var(--paper);
    font-size: 15px;
    line-height: 34px;
    padding-left: 34px;
    white-space: nowrap;
  }

  .card--back .card__ghost-ring {
    left: 100px; top: -10px;
    width: 320px; height: 320px;
    border-color: rgba(0,0,0,.06);
  }
  .back-mark {
    position: absolute;
    left: 220px; top: 70px;
    width: 80px; height: 80px;
    border: 5px solid var(--paper);
    border-radius: 50%;
  }
  .card--back .brand-name {
    left: 0; right: 0; top: 172px;
    text-align: center;
    font-size: 22px;
    color: var(--paper);
  }
</style>
</head>
<body>
  <section class="card card--front" aria-label="Business card front">
    <div class="card__ghost-ring" aria-hidden="true"></div>
    <div class="brand-mark" aria-hidden="true"></div>
    <p class="holder">Name<br>Position</p>
    <ul class="contacts">
      <li>
        <svg class="contacts__icon" viewBox="0 0 18 18" aria-hidden="true">
          <circle cx="9" cy="9" r="9" fill="var(--copper)"/>
          <path d="M6 4.5l2 2.2-1 1.2c.6 1.3 1.6 2.3 2.9 2.9l1.2-1 2.2 2-1.2 1.5C8.6 13 5 9.4 4.5 5.7z" fill="#fff"/>
        </svg>
        +44 0000-000000-00
      </li>
      <li>
        <svg class="contacts__icon" viewBox="0 0 18 18" aria-hidden="true">
          <circle cx="9" cy="9" r="9" fill="var(--copper)"/>
          <rect x="4.5" y="6" width="9" height="6.5" fill="#fff"/>
          <path d="M4.5 6l4.5 3.6L13.5 6" fill="none" stroke="var(--copper)" stroke-width="1"/>
        </svg>
        name@coppertiderecords.co.uk
      </li>
      <li>
        <svg class="contacts__icon" viewBox="0 0 18 18" aria-hidden="true">
          <circle cx="9" cy="9" r="9" fill="var(--copper)"/>
        </svg>
        @CopperTideRecsUK
      </li>
      <li>
        <svg class="contacts__icon" viewBox="0 0 18 18" aria-hidden="true">
          <circle cx="9" cy="9" r="9" fill="var(--copper)"/>
        </svg>
        @CopperTideRecs
      </li>
    </ul>
    <p class="brand-name">Copper Tide Records</p>
    <p class="stripe">www.coppertiderecords.co.uk</p>
  </section>

  <section class="card card--back" aria-label="Business card back">
    <div class="card__ghost-ring" aria-hidden="true"></div>
    <div class="back-mark" aria-hidden="true"></div>
    <p class="brand-name">Copper Tide Records</p>
  </section>
</body>
</html>
```